Logo and Flyer for Co-Branded Comedy Show

Graphic designer needed to create a promotional flyer for a comedy show. Two different comedy shows, with distinct branding, are joining forces to create a combined show. (co-branded logo to be included is attached.)

The design of the promotional materials should be a modern take on a vintage poster a la Quirkwood Jamboree. We'd like it to be a vintage look with a modern twist (I have attached the Quirkwood Jamboree Flyer for reference - marked up with info for our show) Filename: PLGRVN Flyer Mark Up

Images of the two hosts are attached: Filenames:

Our show will be in a theater, so if it can play off a playbill that would be great. I have attached examples of the clean look that we like, as well as some vintage theater flyers. We'd like to stay on the lighter side of the color palette (light gray, blues, etc. which is in line with the Harbor Laughs Live flyer) Filename: PLGR VN Flyer Direction

Current Branding of the individual Shows
I have attached the current promo materials for the individual shows, so you have a sense of the color palette and logo treatment.

The deliverable:
1 flyer vertical, 1 flyer horizontal - same design/concept but in 2 orientation (vertical and horizontal) horizontal will be used for web.
***This flyer will include the co-branded logo seen attached - Harbor Laughs Live Gets Real Honest (individual logos already created and attached) - Download PSD File here: http://lnk.example-short.test/PLGRVN

Industry/Entity Type

Graphic Designer

Colors
0493cd
85cae6
ecf7fb
f5f5f5
ffffff
606060
fbfbfb
0255a3
3176b5

Requirements
Must have
• Vintage look with a modern twist
• Vertical and horizontal options

```html
<!DOCTYPE html>
<html lang="en">
<head>
<meta charset="utf-8">
<title>Harbor Laughs Live Gets Real Honest – Comedy Show</title>
<link rel="stylesheet" href="https://fonts.googleapis.com/css2?family=Courgette&family=Marcellus&display=swap">
<style>
  :root {
    --paper: #e9e2d0;
    --paper-light: #f1ece0;
    --paper-edge: #cfc5ad;
    --tint: #cfd8d8;
    --ink: #141414;
    --ink-soft: #3a3a3a;
    --rule: #3aa6d8;
    --badge: #7cc3df;
    --badge-ink: #ffffff;
    --photo-core: #5d7890;
    --photo-mid: #8aa2b6;
    --photo-edge: #b9c8d3;
  }
  * { margin: 0; padding: 0; box-sizing: border-box; }
  html, body { width: 781px; height: 1200px; overflow: hidden; background: var(--paper); }
  .poster {
    position: relative;
    width: 781px;
    height: 1200px;
    overflow: hidden;
    background:
      radial-gradient(ellipse 70% 55% at 50% 48%, var(--paper-light) 0%, rgba(241,236,224,0) 70%),
      radial-gradient(ellipse 90% 70% at 50% 50%, var(--tint) 0%, var(--paper) 60%, var(--paper-edge) 100%);
    font-family: "Courgette", cursive;
    color: var(--ink-soft);
    text-align: center;
  }
  .badge {
    position: absolute;
    left: -20px;
    top: -30px;
    width: 200px;
    height: 140px;
  }
  .badge-text {
    position: absolute;
    left: 8px;
    top: 10px;
    transform: rotate(-18deg);
    color: var(--badge-ink);
    font-family: "Marcellus", serif;
    line-height: 1.05;
  }
  .badge-text .big { font-size: 21px; }
  .badge-text .small { font-size: 13px; }
  .presenter {
    position: absolute; top: 76px; left: 0; right: 0;
    font-size: 29px; letter-spacing: 0.5px;
  }
  .rule-label {
    position: absolute; left: 37px; right: 37px;
    display: flex; align-items: center; gap: 6px;
    font-size: 20px;
  }
  .rule-label::before, .rule-label::after {
    content: ""; flex: 1; height: 2px; background: var(--rule);
  }
  .presents { top: 135px; }
  .comedy-show { top: 311px; }
  .title {
    position: absolute; left: 0; right: 0;
    font-family: "Marcellus", serif;
    font-weight: 400;
    color: var(--ink);
    font-size: 66px; line-height: 1;
    letter-spacing: 4px;
    white-space: nowrap;
  }
  .title-line-1 { top: 162px; }
  .title-line-2 { top: 234px; }
  .hosted-by { position: absolute; top: 372px; left: 0; right: 0; font-size: 23px; }
  .host-photo { position: absolute; border-radius: 50%; }
  .host-photo-left {
    left: 47px; top: 393px; width: 307px; height: 440px;
    background: radial-gradient(ellipse at center, var(--photo-core) 0%, var(--photo-mid) 62%, var(--photo-edge) 90%, rgba(185,200,211,0) 100%);
  }
  .host-photo-right {
    left: 407px; top: 360px; width: 333px; height: 427px;
    background: radial-gradient(ellipse at center, var(--photo-core) 0%, var(--photo-mid) 62%, var(--photo-edge) 90%, rgba(185,200,211,0) 100%);
  }
  .host-name { position: absolute; top: 876px; font-size: 22px; width: 300px; }
  .host-name-left { left: 50px; }
  .host-name-right { left: 440px; }
  .featuring { position: absolute; top: 940px; left: 0; right: 0; font-size: 35px; color: #222; }
  .lineup { position: absolute; left: 0; right: 0; font-size: 26px; color: #222; white-space: nowrap; }
  .lineup-1 { top: 1008px; }
  .lineup-2 { top: 1044px; }
  .venue {
    position: absolute; left: 16px; right: 16px; top: 1128px; height: 54px;
    border-top: 2px solid var(--rule); border-bottom: 2px solid var(--rule);
    font-size: 36px; line-height: 50px; color: #111; letter-spacing: 0.5px;
    white-space: nowrap;
  }
</style>
</head>
<body>
<main class="poster">
  <svg class="badge" viewBox="0 0 200 140" aria-hidden="true">
    <polygon fill="var(--badge)" points="0,0 200,0 178,40 196,62 160,70 150,100 118,92 100,122 80,100 50,118 40,92 0,100"/>
  </svg>
  <div class="badge-text">
    <div class="big">ONE NIGHT</div>
    <div class="small">Saturday</div>
    <div class="small">August 22, 2015</div>
  </div>

  <p class="presenter">Pale Slate Entertainment</p>
  <p class="rule-label presents">Presents</p>
  <h1 class="title title-line-1">Harbor Laughs Live</h1>
  <h1 class="title title-line-2">Gets Real Honest</h1>
  <p class="rule-label comedy-show">Comedy Show</p>
  <p class="hosted-by">Hosted By</p>

  <div class="host-photo host-photo-left" role="img" aria-label="Portrait photo of host Zolo Brightwave"></div>
  <div class="host-photo host-photo-right" role="img" aria-label="Portrait photo of host Marla Vintrow"></div>

  <p class="host-name host-name-left">Zolo Brightwave</p>
  <p class="host-name host-name-right">Marla Vintrow</p>

  <p class="featuring">Featuring</p>
  <p class="lineup lineup-1">Dev Marrow • Tobias Quillfern • Reuben Calloway</p>
  <p class="lineup lineup-2">Nina Haldorf • Bramwell • Otis Penlow</p>

  <p class="venue">Carousel 418 Meridian Porthaven, NY 10990</p>
</main>
</body>
</html>
```